We are seeking two label designs for our premium pecan snack brand, TORVELLO. TORVELLO is known for its innovative pecan snacks, specifically a healthy and exotic blend of pecans, expertly salted, and infused with unique chili flavors. Our snacks are packaged in stand-up pouch bags, and we are looking for label designs product sizes - 5 oz. ( Size: 14 x 20 cm / 5.5 x 7.8 inches / Max Capacity: 16.2 oz)

Background Information:
TORVELLO is a brand committed to offering a delightful snacking experience that combines the natural richness of pecans with the bold and exotic kick of carefully selected chilies. Our snacks cater to health-conscious consumers who appreciate the fusion of premium quality, unique flavors, and nutritional goodness.

Target Market(s)

Event Attendees (Entertainment Industry), Health-Conscious Consumers

Industry/Entity Type

Entertainment (sports events, arenas, stadiums, etc)

Font styles to use
Other font styles liked:
• Brother1816 Printed

Colors

Designer to choose colors to be used in the design.

Requirements
Must have
• Nutrition Fact (attached) , TRANSPARENT PART LIKE A WINDOW TO DISPLAY THE PRODUCT

```html
<!DOCTYPE html>
<html lang="en">
<head>
<meta charset="utf-8">
<title>Torvello Spicy Roasted Pecans – Pouch Label</title>
<link rel="stylesheet" href="https://fonts.googleapis.com/css2?family=Montserrat:wght@400;500;600&display=swap">
<style>
  :root {
    --backdrop: #959595;
    --pouch-black: #111111;
    --pouch-orange: #d9653b;
    --accent-orange: #e0774a;
    --illustration-tone: #dd6f45;
    --ink-white: #f2f2f2;
    --pecan-light: #d7a27a;
    --pecan-dark: #8a5430;
    --seal-line: #262626;
  }
  html, body {
    margin: 0;
    padding: 0;
    width: 1200px;
    height: 800px;
    overflow: hidden;
    background: var(--backdrop);
  }
  .canvas {
    display: block;
    width: 1200px;
    height: 800px;
  }
  .brand-name {
    font-family: "Montserrat", sans-serif;
    font-weight: 600;
    font-size: 42px;
    letter-spacing: 2px;
    fill: var(--ink-white);
  }
  .brand-byline {
    font-family: "Montserrat", sans-serif;
    font-weight: 400;
    font-size: 9px;
    letter-spacing: 0.3px;
    fill: var(--ink-white);
  }
  .product-line {
    font-family: "Montserrat", sans-serif;
    font-weight: 500;
    font-size: 19px;
    letter-spacing: 1.6px;
  }
  .product-line--white { fill: var(--ink-white); }
  .product-line--orange { fill: var(--accent-orange); }
  .net-weight {
    font-family: "Montserrat", sans-serif;
    font-weight: 400;
    font-size: 9.5px;
    letter-spacing: 0.4px;
    fill: var(--ink-white);
  }
</style>
</head>
<body>
<svg class="canvas" viewBox="0 0 1200 800" xmlns="http://www.w3.org/2000/svg">
  <defs>
    <clipPath id="pouch-shape">
      <path d="M406 81 H786 Q801 81 801 96 V420 Q800 560 775 680 Q772 715 745 720 Q600 732 447 720 Q422 715 420 680 Q396 560 391 420 V96 Q391 81 406 81 Z"/>
    </clipPath>
    <clipPath id="window-shape">
      <rect x="440" y="518" width="320" height="160"/>
    </clipPath>
    <linearGradient id="pecan-fill" x1="0" y1="0" x2="0" y2="1">
      <stop offset="0" stop-color="#b06d42"/>
      <stop offset="0.5" stop-color="#d7a27a"/>
      <stop offset="1" stop-color="#b9784d"/>
    </linearGradient>
  </defs>

  <g class="pouch" clip-path="url(#pouch-shape)">
    <rect class="pouch-top" x="380" y="70" width="440" height="440" fill="var(--pouch-black)"/>
    <rect class="pouch-top-pattern" x="380" y="70" width="440" height="96" fill="#141414"
          role="img" aria-label="Faint line drawings of chilies, flames and pecans on the top band"/>
    <rect class="zip-seal" x="391" y="163" width="410" height="3" fill="var(--seal-line)"/>
    <rect class="pouch-base" x="380" y="505" width="440" height="240" fill="var(--pouch-orange)"/>
  </g>

  <g class="product-window">
    <circle class="window-badge" cx="595" cy="531" r="138" fill="var(--pouch-orange)"/>
    <ellipse class="window-illustration" cx="595" cy="456" rx="72" ry="54" fill="var(--illustration-tone)"
             role="img" aria-label="White line drawing of a pecan and chili pepper in flames"/>
    <circle class="window-clear" cx="595" cy="531" r="138" fill="url(#pecan-fill)"
            clip-path="url(#window-shape)" role="img" aria-label="Clear window showing roasted pecan halves"/>
  </g>

  <g class="brand">
    <text class="brand-name" x="596" y="265" text-anchor="middle">TORVELLO</text>
    <text class="brand-byline" x="680" y="282" text-anchor="end">BY HALDEN</text>
  </g>

  <g class="product-title">
    <text class="product-line product-line--white" x="595" y="342" text-anchor="middle">SPICY ROASTED</text>
    <text class="product-line product-line--orange" x="595" y="365" text-anchor="middle">PECANS</text>
  </g>

  <text class="net-weight" x="595" y="684" text-anchor="middle">5 oz (142gr)</text>
</svg>
</body>
</html>
```